Clean Menu Design for Healthy Lifestyle Restaurant

Please design a menu that looks clean and bright . Take a look at the website www.morvelbistro.com for brand vibes and colours.
We need all items on the menu(attached), with a cover page that includes our Logo(attached), address(4318 52nd Avenue SW, Calgary AB, T3K4H8), phone number(825-614-3872) and website(www.morvelbistro.com . A photo should also be on the cover. I have attached some photos that you can choose from, as well as use throughout the design if you want.
Ensure the file is either letter size or legal size, and trifold is needed to fit all of the items. Items and pages should be a similar order as to the old menu we had designed. Please see attached.

```html
<!DOCTYPE html>
<html lang="en">
<head>
<meta charset="utf-8">
<title>Morvel Bistro Menu</title>
<link href="https://fonts.googleapis.com/css2?family=Francois+One&family=Open+Sans:wght@400;600;700&display=swap" rel="stylesheet">
<style>
:root{
  --bg:#8f8f8f;
  --paper:#f4f4f5;
  --ink:#2c2c2c;
  --brand-green:#7bb928;
  --carbs:#f8cb93;
  --sauce:#eaa6b4;
  --treats:#a9cbe8;
  --packages:#7cc02a;
  --yellow:#efd77c;
  --red:#f26f5e;
  --purple:#cb97e2;
  --salmon:#f7956d;
  --green:#7dc86a;
  --orange:#f48a5e;
  --teal:#5fd0aa;
  --tan:#c8a46d;
}
*{margin:0;padding:0;box-sizing:border-box}
html,body{width:900px;height:1200px;overflow:hidden}
body{background:var(--bg);font-family:"Open Sans",Arial,sans-serif;color:var(--ink);position:relative}
.sheet{position:absolute;background:var(--paper);overflow:hidden}
.sheet-outside{left:22px;top:33px;width:675px;height:524px}
.sheet-inside{left:125px;top:580px;width:713px;height:555px}
.panel{position:absolute;top:0;height:100%}
.panel-shade{background:linear-gradient(90deg,#e6e7e8 0,#f6f6f7 12%,#f6f6f7 88%,#e9eaea 100%)}
.cover{background:linear-gradient(180deg,#f7f7f8 0,#e9ebec 45%,#f3f3f4 100%)}
.photo{position:absolute;border-radius:6px}
.banner{position:absolute;display:flex;flex-direction:column;justify-content:center;padding-left:22px;font-family:"Francois One",Impact,sans-serif;text-transform:uppercase;color:#2a2a2a;line-height:1}
.banner.lg{font-size:20px}
.banner.md{font-size:17px;line-height:.95}
.banner.sm{font-size:12px;line-height:1.05}
.menu-list{position:absolute;list-style:none;font-size:7px;color:#333}
.menu-list li{display:flex;align-items:flex-end;white-space:nowrap}
.menu-list .dots{flex:1;border-bottom:1px dotted #999;margin:0 1px 2px}
.rule{position:absolute;height:1px;background:#888}
.brand{position:absolute;text-align:center;font-family:"Francois One",Impact,sans-serif;color:var(--brand-green)}
.brand .mark{display:inline-block;width:9px;height:9px;border-radius:50%;background:var(--brand-green);margin-right:4px;vertical-align:middle}
.brand .tag{display:block;font-family:"Open Sans",Arial,sans-serif;font-weight:700;color:var(--brand-green);letter-spacing:.3px}
.contact{position:absolute;text-align:center;font-size:7.5px;color:#333;line-height:12px}
.contact-row{display:flex;align-items:center;gap:4px;justify-content:flex-start}
.heading{position:absolute;text-align:center;font-family:"Francois One",Impact,sans-serif;color:#222}
.store-badge{position:absolute;width:44px;height:14px;background:#111;border-radius:3px}
.note{position:absolute;font-size:5.3px;line-height:7px;text-align:center;color:#333}
</style>
</head>
<body>

<section class="sheet sheet-outside">
  <div class="panel panel-shade" style="left:0;width:225px">
    <div class="photo" role="img" aria-label="Meal prep container of pasta with grated cheese" style="left:18px;top:0;width:100px;height:98px;background:radial-gradient(circle at 50% 50%,#c9752f 0,#a3501f 45%,#1d1d1d 70%)"></div>
    <div class="banner md" style="left:16px;top:104px;width:194px;height:40px;background:var(--carbs)"><span>Carbs</span><span>100g $3/200g $5</span></div>
    <ul class="menu-list" style="left:22px;top:150px;width:200px;line-height:12.4px">
      <li><span>Baby Potato</span></li>
      <li><span>Sweet Potato</span></li>
      <li><span>Pesto Pasta</span><span class="dots"></span><span>+ $1</span></li>
      <li><span>Tomato pasta</span><span class="dots"></span><span>+ $1</span></li>
      <li><span>Brown Rice</span></li>
      <li><span>Basmati Rice</span></li>
      <li><span>Quinoa</span></li>
      <li><span>Mashed Potato</span></li>
      <li><span>Mashed Sweet Potato</span></li>
    </ul>
    <div class="photo" role="img" aria-label="Container of roasted sweet potato wedges" style="left:126px;top:214px;width:88px;height:58px;background:radial-gradient(circle,#d1642a 0,#a94318 50%,#1f1f1f 75%)"></div>
    <div class="banner md" style="left:0;top:274px;width:210px;height:42px;background:var(--sauce)"><span>Meal Prep Sauce</span><span>Options</span></div>
    <ul class="menu-list" style="left:22px;top:326px;width:200px;line-height:11.9px">
      <li><span>Ancho Chipotle Sauce</span><span class="dots"></span><span>$1</span></li>
      <li><span>Spicy Mayo</span><span class="dots"></span><span>$1</span></li>
      <li><span>BBQ Sauce</span><span class="dots"></span><span>$1</span></li>
      <li><span>Thai Sauce</span><span class="dots"></span><span>$1</span></li>
      <li><span>Teriyaki Sauce</span><span class="dots"></span><span>$1</span></li>
      <li><span>Hot Sauce</span><span class="dots"></span><span>$1</span></li>
      <li><span>Pesto sauce</span><span class="dots"></span><span>$1.50</span></li>
      <li><span>Tomato Sauce</span><span class="dots"></span><span>$1</span></li>
      <li><span>Sesame Ginger</span><span class="dots"></span><span>$1.25</span></li>
      <li><span>Balsamic Dressing</span><span class="dots"></span><span>$1</span></li>
      <li style="width:110px"><span>Hoisin Dressing</span><span class="dots"></span><span>$1</span></li>
    </ul>
    <div class="photo" role="img" aria-label="Plate of glazed salmon with green beans" style="left:123px;top:457px;width:105px;height:62px;border-radius:50%;background:radial-gradient(circle,#b5532a 0,#d98a4a 30%,#f2f2f2 60%,#e4e4e4 100%)"></div>
  </div>

  <div class="panel panel-shade" style="left:225px;width:220px">
    <div class="photo" role="img" aria-label="Plate of white chocolate bites and cookies" style="left:105px;top:4px;width:93px;height:56px;background:radial-gradient(circle,#e8d3c0 0,#c99a84 45%,#f0f0f0 75%)"></div>
    <div class="banner lg" style="left:0;top:60px;width:211px;height:28px;background:var(--treats);color:#2f3d4c"><span>Treats</span></div>
    <ul class="menu-list" style="left:16px;top:96px;width:190px;line-height:12px">
      <li><span>White Chocolate Bites</span><span class="dots"></span><span>$1.95</span></li>
      <li><span>Coconut Cream Cookie</span><span class="dots"></span><span>$3.50</span></li>
      <li><span>Protein Carrot Cake</span><span class="dots"></span><span>$5.45</span></li>
    </ul>
    <div class="photo" role="img" aria-label="Stack of protein pancakes with berries" style="left:98px;top:134px;width:70px;height:48px;border-radius:50%;background:radial-gradient(circle,#c98e52 0,#e6c08c 35%,#f4f4f4 65%)"></div>
    <div class="banner lg" style="left:0;top:192px;width:211px;height:27px;background:var(--packages)"><span>Packages</span></div>
    <ul class="menu-list" style="left:16px;top:228px;width:190px;line-height:12px">
      <li><span>Bronze</span><span class="dots"></span><span>$100 ($5 in points)</span></li>
      <li><span>Silver</span><span class="dots"></span><span>$300 ($15 in points)</span></li>
      <li><span>Gold</span><span class="dots"></span><span>$600 ($60 in points)</span></li>
      <li><span>Platinum</span><span class="dots"></span><span>$1000 ($150 in points)</span></li>
    </ul>
    <div class="rule" style="left:15px;top:298px;width:194px"></div>
    <div class="brand" style="left:0;top:306px;width:220px;font-size:19px;line-height:20px"><span class="mark"></span>MORVEL<span class="tag" style="font-size:5.5px;line-height:8px">BISTRO | MEAL PREP</span></div>
    <div class="heading" style="left:0;top:345px;width:220px;font-size:14px">CONTACT US</div>
    <div class="contact" style="left:62px;top:377px;width:120px">
      <div class="contact-row"><svg width="8" height="8" viewBox="0 0 10 10"><circle cx="5" cy="5" r="4" fill="none" stroke="#333" stroke-width="1.2"/><path d="M1 5h8M5 1c-2 2.5-2 5.5 0 8M5 1c2 2.5 2 5.5 0 8" fill="none" stroke="#333" stroke-width=".8"/></svg><span>www.morvelbistro.com</span></div>
      <div class="contact-row"><svg width="8" height="8" viewBox="0 0 10 10"><rect x="0" y="0" width="10" height="10" rx="2" fill="#333"/><path d="M3 2.5l1 1.5-.7.8c.4 1 1.2 1.8 2.2 2.2l.8-.7 1.5 1-.6 1.2C5 8.3 1.8 5 2 2.9z" fill="#fff"/></svg><span>825.614.3872</span></div>
      <div class="contact-row"><svg width="8" height="8" viewBox="0 0 10 10"><path d="M2 1v8M2 1h6l-2 2 2 2H2" fill="#333" stroke="#333" stroke-width="1"/></svg><span>4318 52nd Avenue SW,</span></div>
      <div class="contact-row" style="padding-left:12px"><span>Calgary AB, T3K4H8</span></div>
    </div>
    <div class="store-badge" style="left:61px;top:437px"></div>
    <div class="store-badge" style="left:118px;top:437px"></div>
    <div class="rule" style="left:15px;top:457px;width:194px"></div>
    <p class="note" style="left:17px;top:460px;width:188px">Use your points to receive discounts online. If purchasing a package in store we will add the extra money to your account. You can order in-store, over the phone, or online. If you have an issue please call the location nearest you and we will be happy to help.</p>
  </div>

  <div class="panel cover" style="left:445px;width:230px">
    <div class="brand" style="left:0;top:47px;width:230px;font-size:29px;line-height:28px"><span class="mark" style="width:12px;height:12px"></span>MORVEL<span class="tag" style="font-size:8px;line-height:11px">BISTRO | MEAL PREP</span></div>
    <div class="photo" role="img" aria-label="Bowl of salad topped with sliced grilled chicken" style="left:3px;top:182px;width:227px;height:145px;border-radius:50%;background:radial-gradient(ellipse at 55% 45%,#d79a5e 0,#c0703f 18%,#6f9a3a 38%,#b8414a 52%,#eeeeee 72%,#e3e5e6 100%)"></div>
    <div class="heading" style="left:0;top:398px;width:230px;font-size:20px;letter-spacing:1px">MENU</div>
    <div class="rule" style="left:38px;top:431px;width:157px"></div>
    <div class="contact" style="left:0;top:440px;width:230px;line-height:12px">www.morvelbistro.com<br>825.614.3872<br>4318 52nd Avenue SW,<br>Calgary AB, T3K4H8</div>
    <div class="rule" style="left:38px;top:493px;width:157px"></div>
  </div>
</section>

<section class="sheet sheet-inside">
  <div class="panel panel-shade" style="left:0;width:237px">
    <div class="banner sm" style="left:0;top:20px;width:222px;height:33px;background:var(--yellow)"><span>Morvel Bistro</span><span>Meal Prep</span></div>
    <div class="banner lg" style="left:0;top:58px;width:222px;height:30px;background:var(--red)"><span>Pre-Built Meals</span></div>
    <ul class="menu-list" style="left:23px;top:97px;width:208px;line-height:13.9px">
      <li><span>Asian Chicken Teriyaki</span><span class="dots"></span><span>$13.45</span></li>
      <li><span>BBQ Glazed Salmon</span><span class="dots"></span><span>$16.95</span></li>
      <li style="width:135px"><span>Butter Chicken</span><span class="dots"></span><span>$13.95</span></li>
      <li style="width:135px"><span>Chicken Parmesan</span><span class="dots"></span><span>$13.95</span></li>
      <li style="width:135px"><span>Chicken Alfredo</span><span class="dots"></span><span>$13.45</span></li>
      <li style="width:135px"><span>Stuffed Chicken</span><span class="dots"></span><span>$14.95</span></li>
      <li style="width:135px"><span>Pesto Chicken Penne</span><span class="dots"></span><span>$13.45</span></li>
      <li><span>Steak N Green Stir-fry</span><span class="dots"></span><span>$13.45</span></li>
      <li><span>Turkey Meatball Fettuccine</span><span class="dots"></span><span>$13.45</span></li>
      <li><span>Creamy Peanut Chicken</span><span class="dots"></span><span>$14.95</span></li>
      <li><span>Demi Chicken</span><span class="dots"></span><span>$15.45</span></li>
      <li><span>Cheesy Buffalo Salmon</span><span class="dots"></span><span>$16.95</span></li>
      <li><span>Bolognese Pasta</span><span class="dots"></span><span>$13.95</span></li>
      <li><span>Taco Bowl</span><span class="dots"></span><span>$13.95</span></li>
      <li><span>Coconut Garlic Shrimp</span><span class="dots"></span><span>$15.95</span></li>
      <li><span>Pesto Chicken Pizza</span><span class="dots"></span><span>$10.95</span></li>
      <li><span>Texas Pizza</span><span class="dots"></span><span>$10.95</span></li>
      <li><span>Original Chicken Pizza</span><span class="dots"></span><span>$10.95</span></li>
      <li><span>BBQ Chicken Pizza</span><span class="dots"></span><span>$10.95</span></li>
      <li><span>Creamy Mushroom Steak Bites</span><span class="dots"></span><span>$15.45</span></li>
      <li><span>Cheese Burger Bowl</span><span class="dots"></span><span>$13.45</span></li>
      <li><span>Pesto Chicken Quesadilla</span><span class="dots"></span><span>$13.45</span></li>
      <li><span>Ancho Chipotle Steak Wrap</span><span class="dots"></span><span>$12.45</span></li>
      <li><span>BBQ Chicken Wrap</span><span class="dots"></span><span>$12.45</span></li>
      <li style="width:145px"><span>Chicken Tzatziki Wrap</span><span class="dots"></span><span>$11.45</span></li>
      <li style="width:140px"><span>Chicken Panini</span><span class="dots"></span><span>$13.45</span></li>
      <li style="width:140px"><span>Mekong Wrap</span><span class="dots"></span><span>$13.45</span></li>
    </ul>
    <div class="photo" role="img" aria-label="Bowl of chicken salad" style="left:163px;top:124px;width:64px;height:50px;border-radius:50%;background:radial-gradient(circle,#d9a165 0,#7da93c 40%,#efefef 70%)"></div>
    <div class="photo" role="img" aria-label="Halved chicken wraps" style="left:172px;top:428px;width:58px;height:50px;border-radius:50%;background:radial-gradient(circle,#c78e55 0,#e5c79c 40%,#f1f1f1 70%)"></div>
    <div class="banner lg" style="left:0;top:480px;width:222px;height:30px;background:var(--purple)"><span>Breakfast</span></div>
    <ul class="menu-list" style="left:23px;top:519px;width:208px">
      <li><span>Blueberry Protein Pancakes</span><span class="dots"></span><span>$12.95</span></li>
    </ul>
  </div>

  <div class="panel panel-shade" style="left:237px;width:236px">
    <ul class="menu-list" style="left:10px;top:19px;width:206px;line-height:13px">
      <li><span>Chocolate Protein Pancakes</span><span class="dots"></span><span>$12.95</span></li>
      <li><span>Plain Protein Pancakes</span><span class="dots"></span><span>$11.95</span></li>
      <li><span>Bacon, egg, cheese Scrambler</span><span class="dots"></span><span>$12.4</span></li>
      <li><span>Meat Omelette</span><span class="dots"></span><span>$12.95</span></li>
      <li><span>Veggie Omelette</span><span class="dots"></span><span>$11.95</span></li>
      <li style="width:148px"><span>Rise N Grind Burrito</span><span class="dots"></span><span>$11.95</span></li>
      <li style="width:152px"><span>Peanut Butter Overnight Oats</span><span class="dots"></span><span>$6.95</span></li>
      <li><span>Cranberry Pecan Overnight Oats</span></li>
    </ul>
    <div class="photo" role="img" aria-label="Pancakes with berries" style="left:168px;top:90px;width:60px;height:32px;border-radius:50%;background:radial-gradient(circle,#c2874d 0,#4b5e9a 35%,#efefef 65%)"></div>
    <div class="banner lg" style="left:0;top:132px;width:218px;height:29px;background:var(--salmon)"><span>Protein Bundles</span></div>
    <ul class="menu-list" style="left:10px;top:169px;width:206px;line-height:12.8px">
      <li><span>16oz Chicken</span><span class="dots"></span><span>$18</span></li>
      <li><span>16oz Bison</span><span class="dots"></span><span>$24</span></li>
      <li><span>16oz Salmon</span><span class="dots"></span><span>$24</span></li>
      <li><span>16oz Steak Bite</span><span class="dots"></span><span>$27</span></li>
      <li><span>16oz Ground Beef</span><span class="dots"></span><span>$18</span></li>
      <li><span>16oz Ground Turkey</span><span class="dots"></span><span>$18</span></li>
      <li><span>16oz Turkey Bites</span><span class="dots"></span><span>$20</span></li>
    </ul>
    <div class="banner lg" style="left:0;top:270px;width:218px;height:29px;background:var(--green)"><span>Veggie Bundles</span></div>
    <ul class="menu-list" style="left:10px;top:307px;width:206px;line-height:12.8px">
      <li><span>16oz Broccoli</span><span class="dots"></span><span>$10</span></li>
      <li><span>16oz Carrots N Peas</span><span class="dots"></span><span>$7</span></li>
      <li><span>16oz Cauliflower</span><span class="dots"></span><span>$9.50</span></li>
      <li><span>16oz Mixed Peppers</span><span class="dots"></span><span>$10.50</span></li>
      <li><span>16oz Mixed Veggies</span><span class="dots"></span><span>$12</span></li>
      <li><span>16oz Seasonal Veggies</span><span class="dots"></span><span>$10.50</span></li>
    </ul>
    <div class="banner lg" style="left:0;top:397px;width:218px;height:29px;background:var(--orange)"><span>Carb Bundles</span></div>
    <ul class="menu-list" style="left:10px;top:432px;width:206px;line-height:13.2px">
      <li><span>16oz Brown Rice</span><span class="dots"></span><span>$7</span></li>
      <li><span>16oz Basmati Rice</span><span class="dots"></span><span>$7</span></li>
      <li><span>16oz Sweet Potato</span><span class="dots"></span><span>$9</span></li>
      <li><span>16oz Roasted Potato</span><span class="dots"></span><span>$9</span></li>
      <li style="width:188px"><span>16oz Mashed Potato</span><span class="dots"></span><span>$9</span></li>
      <li style="width:140px"><span>16oz Sweet Potato Mash</span><span class="dots"></span><span>$9</span></li>
      <li style="width:140px"><span>16oz Pesto Pasta</span><span class="dots"></span><span>$9.50</span></li>
      <li style="width:120px"><span>16oz Quinoa</span><span class="dots"></span><span>$7.50</span></li>
    </ul>
    <div class="photo" role="img" aria-label="Plate of pesto pasta" style="left:153px;top:506px;width:75px;height:40px;border-radius:50%;background:radial-gradient(circle,#b4a34a 0,#7d8f34 35%,#efefef 65%)"></div>
  </div>

  <div class="panel panel-shade" style="left:473px;width:240px">
    <div class="photo" role="img" aria-label="Bowls of grilled protein, rice and vegetables" style="left:62px;top:0;width:178px;height:76px;border-radius:0;background:linear-gradient(90deg,#e9ecec 0,#c3793a 20%,#6b9a3f 45%,#d1a76b 70%,#8cab58 100%)"></div>
    <div class="banner sm" style="left:0;top:76px;width:212px;height:24px;background:var(--yellow)"><span>Custom Build Your Own Meal</span></div>
    <div class="banner lg" style="left:0;top:104px;width:212px;height:29px;background:var(--teal)"><span>Protein Options</span></div>
    <ul class="menu-list" style="left:10px;top:140px;width:204px;line-height:13.1px">
      <li><span>4oz Steak Bites</span><span class="dots"></span><span>$6</span></li>
      <li><span>5oz Turkey Bites</span><span class="dots"></span><span>$5.25</span></li>
      <li><span>5oz Ground Beef</span><span class="dots"></span><span>$5.75</span></li>
      <li><span>5oz Ground Bison</span><span class="dots"></span><span>$7.50</span></li>
      <li><span>4oz Ground Turkey</span><span class="dots"></span><span>$4.95</span></li>
      <li><span>6oz Chicken Breast</span><span class="dots"></span><span>$5.95</span></li>
      <li><span>6oz Salmon</span><span class="dots"></span><span>$8.50</span></li>
      <li><span>5oz Shrimp</span><span class="dots"></span><span>$7</span></li>
      <li><span>8oz Striploin Steak</span><span class="dots"></span><span>$9.95</span></li>
      <li><span>6oz Ahi Tuna</span><span class="dots"></span><span>$9.50</span></li>
      <li><span>Tofu</span><span class="dots"></span><span>$5.50</span></li>
    </ul>
    <div class="banner md" style="left:0;top:298px;width:212px;height:42px;background:var(--tan)"><span>Veggie Options</span><span>100g or 200g</span></div>
    <ul class="menu-list" style="left:10px;top:348px;width:204px;line-height:13px">
      <li><span>Asparagus</span><span class="dots"></span><span>$3.50/$4.75</span></li>
      <li><span>Bell Pepper Mix</span><span class="dots"></span><span>$3/$4.50</span></li>
      <li><span>Broc/Cauli</span><span class="dots"></span><span>$3/$4.50</span></li>
      <li><span>Broccoli</span><span class="dots"></span><span>$3/$4.50</span></li>
      <li><span>Carrots &amp; Peas</span><span class="dots"></span><span>$3/$4.50</span></li>
      <li><span>Carrots</span><span class="dots"></span><span>$3/$4.50</span></li>
      <li><span>Cauliflower</span><span class="dots"></span><span>$3/$4.50</span></li>
      <li><span>Green Beans</span><span class="dots"></span><span>$3/$4.50</span></li>
      <li style="width:126px"><span>Green Mix</span><span class="dots"></span><span>$3/$4.50</span></li>
      <li style="width:126px"><span>Peas</span><span class="dots"></span><span>$3/$4.50</span></li>
      <li style="width:126px"><span>Seasonal Veggies</span><span class="dots"></span><span>$3/$4.50</span></li>
      <li style="width:120px"><span>Pecan Salad</span><span class="dots"></span><span>$4.95/$6.95</span></li>
      <li style="width:116px"><span>Spinach Salad</span><span class="dots"></span><span>$4.95/$6.95</span></li>
    </ul>
    <div class="photo" role="img" aria-label="Container of steamed broccoli" style="left:144px;top:462px;width:96px;height:80px;background:radial-gradient(circle,#5f9a2f 0,#3f7a22 50%,#1c1c1c 75%)"></div>
  </div>
</section>

</body>
</html>
```